Health & Nutrition - Business Cards

Needs to look new-age, simple, and elegant. The cards are for my services/counsel in health and nutrition - which include mind, body, and soul. I would like to see something clean and simple but beautiful. Can have a plain background or with a pattern but I don't want it to take away from my contact details. Therefore, my info can be on the back of the card and a nice front design. I really like the flower of life symbol. The name of my business is called Willow Lantern.

Target Market(s)

Clients - men & women age 20-60. Adults, parents, teachers, sick individuals seeking nutrient counseling and dietary management.

Industry/Entity Type

Nutritionist

Contact Information for Business Card

Tomas Brindle
Cell: 345-582-7046
Email: tbrindle@mailvane.net

Colors
33a6d7
33b8a4
add136
ffffff
5c5c5c
f04a50
fbee3f
cedeed
85cae6

Requirements
Nice to have
• Maybe it can have some sort of sacred geometry as well, but not required. Nice to have the colors that I choose in the project but feel free to come up with your own use of colors. Thanks! =)

```html
<!DOCTYPE html>
<html lang="en">
<head>
<meta charset="utf-8">
<title>Willow Lantern – Business Cards</title>
<link rel="stylesheet" href="https://fonts.googleapis.com/css2?family=Tinos:wght@400;700&family=Arimo:wght@400&display=swap">
<style>
  :root {
    --stage: #2b2b2e;
    --card-dark: #5c5c5c;
    --card-light: #ffffff;
    --ink: #5c5c5c;
    --ink-soft: #6a6a6a;
    --leaf: #add136;
    --leaf-deep: #8fb32a;
  }
  * { margin: 0; padding: 0; box-sizing: border-box; }
  html, body { width: 1200px; height: 800px; overflow: hidden; background: var(--stage); }
  .canvas { position: relative; width: 1200px; height: 800px; }

  .card {
    position: absolute;
    width: 540px;
    height: 309px;
    overflow: hidden;
    box-shadow: 0 12px 30px rgba(0,0,0,.45);
  }

  /* Front */
  .card--front { left: 60px; top: 90px; background: var(--card-dark); }
  .front-brand {
    position: absolute; inset: 0;
    display: flex; align-items: center; justify-content: center; gap: 16px;
  }
  .brand-dot {
    width: 34px; height: 34px; border-radius: 50%;
    background: var(--leaf);
  }
  .front-brand .brand-name {
    font-family: "Tinos", serif; font-weight: 400;
    font-size: 38px; color: var(--card-light); letter-spacing: .5px;
  }

  /* Back */
  .card--back { left: 600px; top: 400px; background: var(--card-light); }
  .back-decoration {
    position: absolute; right: -90px; top: -70px;
    width: 330px; height: 330px; border-radius: 50%;
    background: radial-gradient(circle, var(--leaf) 0%, var(--leaf) 30%, rgba(173,209,54,.55) 55%, rgba(92,92,92,.25) 100%);
  }
  .back-details { position: absolute; left: 36px; bottom: 34px; }
  .back-details .brand-name {
    font-family: "Tinos", serif; font-weight: 400;
    font-size: 30px; color: var(--ink); margin-bottom: 18px;
  }
  .person-name {
    font-family: "Tinos", serif; font-weight: 700;
    font-size: 20px; color: var(--ink-soft); margin-bottom: 8px;
  }
  .contact-list { list-style: none; }
  .contact-item {
    display: flex; align-items: center; gap: 8px;
    font-family: "Arimo", sans-serif; font-size: 14px;
    color: var(--ink); line-height: 1.7;
  }
  .contact-icon { width: 16px; height: 16px; flex: none; }
</style>
</head>
<body>
<main class="canvas">

  <section class="card card--front" aria-label="Card front">
    <div class="front-brand">
      <span class="brand-dot" aria-hidden="true"></span>
      <span class="brand-name">Willow Lantern</span>
    </div>
  </section>

  <section class="card card--back" aria-label="Card back">
    <div class="back-decoration" role="img" aria-label="Large green and grey botanical decoration"></div>
    <div class="back-details">
      <p class="brand-name">Willow Lantern</p>
      <p class="person-name">Tomas Brindle</p>
      <ul class="contact-list">
        <li class="contact-item">
          <svg class="contact-icon" viewBox="0 0 16 16" aria-hidden="true">
            <circle cx="8" cy="8" r="7.5" fill="none" stroke="var(--leaf)" stroke-width="1"/>
            <rect x="5.5" y="3.5" width="5" height="9" rx="1" fill="none" stroke="var(--leaf-deep)" stroke-width="1.2"/>
            <circle cx="8" cy="11" r=".7" fill="var(--leaf-deep)"/>
          </svg>
          345-582-7046
        </li>
        <li class="contact-item">
          <svg class="contact-icon" viewBox="0 0 16 16" aria-hidden="true">
            <circle cx="8" cy="8" r="8" fill="var(--leaf)"/>
            <rect x="4" y="5.2" width="8" height="5.6" fill="none" stroke="#fff" stroke-width="1.1"/>
            <polyline points="4,5.4 8,8.6 12,5.4" fill="none" stroke="#fff" stroke-width="1.1"/>
          </svg>
          tbrindle@mailvane.net
        </li>
      </ul>
    </div>
  </section>

</main>
</body>
</html>
```